Blogging Platform for Christian Missions

We need the main (one) page design for FaithPostly. FaithPostly is a blogging platform for people (missionaries) who work for Christian Mission organisations in various countries. It will provides an easy way for them to setup and maintain a blog that will have features specifically for missions.

There's a lot of work involved in creating a web page design so I am happy to receive many quick rough designs. I will select my favourite four or five designs and these can submit the full design.

Please see the attached wireframe. Please also see the attached logo.

Main colours
- black
- white
- grey
- red (see logo colour) can be used occasionally eg. titles
- another complementary colour - occasionally used

Photos uploaded by the missionaries will provide colour for the website.

It needs to be a clean design that is not cluttered. The main focus are the blog posts. The information on the side complements the blog. There are navigational options at the top and bottom. The FaithPostly logo is not the main focus. The person's name (blog owner) is what needs to be most prominent.

I love the BrightNoma design (http://www.brightnoma-demo.net/). I particularly like the soft design - light grey background, white background boxes for content. The focus is the content - text and photos. I also like the subtle use of breakout image - "Step into the Venture". I like the black navigation header and the black footer. I do not want a exact copy of the site but I'd like to use this concept .

I also like this Quibbly design (http://calm.quibbly-demo.net/theme/preview/5193) because of the white box (and the shadow) for the content. I also like how the word "Quote" and the number of "notes" breaks out of the white content area (see attachment). I'd like to do this, if possible with the date. This is just a "nice to have" - definitely not essential. I don't like the font for the title in this example.

We have build a simple prototype already. I cautiously show this because I want the the design of this to be completely ignored. I used a free template. Along with the wireframe this prototype should an idea of what kind of content will be displayed but please don't look too much at it.
http://faithpostly-demo.org/blog/1

The design will be used to create a website using Verdant. We will use zScript so feel free to suggest an animation or lightbox effect to make your design more dynamic. This is a nice to have.

Once we have our final design we will need to define the style for:
- h1 through h4 tags
- Paragraphs
- Lists
- Block quotes
- Italics, bolding and underlining
- Links, including active, hover and visited states

Please let me know what additional information you need. Also let me know if there is something I have not considered.

Target Market(s)

The target customers are mission workers aged 25-35 who will post blog entries. These posts will be read by their friends and family.

Requirements
Must have
• Clean simple design. Must be inspired by the BrightNoma (http://www.brightnoma-demo.net/) design without copying it.
Nice to have
• Design element that breaks out of the boxes. See the screenshot attached from the Quibbly site. Described more in the project overview.
Should not have
• Should not use fonts that are not web-friendly. Should not have features that will be difficult to implement using HTML/CSS.

```html
<!DOCTYPE html>
<html lang="en">
<head>
<meta charset="utf-8">
<title>Hannah Brooks – Mission Blog</title>
<link rel="stylesheet" href="https://fonts.googleapis.com/css2?family=Arimo:wght@400;700&family=Crimson+Text:ital@1&display=swap">
<style>
:root{
  --ink:#333;
  --text:#3c3c3c;
  --muted:#9a9a9a;
  --faint:#b5b5b5;
  --red:#e3001b;
  --rose:#e7677a;
  --nav:#3b3b3b;
  --foot:#2b2b2b;
  --page:#ebebeb;
  --side:#f4f4f4;
  --line:#dcdcdc;
  --white:#fff;
}
*{box-sizing:border-box;margin:0;padding:0}
html,body{width:825px;height:1200px;overflow:hidden}
body{position:relative;background:var(--page);font-family:"Arimo",Arial,sans-serif;color:var(--text)}
.abs{position:absolute}
ul{list-style:none}

/* top navigation */
.topbar{left:0;top:0;width:825px;height:25px;background:var(--nav)}
.topbar .mark{left:58px;top:5px}
.topbar .menu{left:87px;top:0;display:flex;height:25px}
.topbar .menu a{color:var(--white);font-size:10.5px;text-decoration:none;line-height:25px;padding:0 10px;text-transform:uppercase}
.topbar .menu a.active{background:var(--red);padding:0 9px}
.topbar .account{right:50px;top:0;line-height:25px;font-size:10.5px;color:var(--white)}
.topbar .account span{margin:0 8px;color:#aaa}

/* header */
.masthead{left:0;top:25px;width:825px;height:96px;background:var(--white);border-bottom:1px solid #e2e2e2}
.owner-name{left:56px;top:18px;font-size:37px;color:var(--red);line-height:1}
.owner-org{left:56px;top:58px;font-size:22px;color:var(--muted);font-weight:700;line-height:1}
.search{left:585px;top:43px;width:185px;height:21px;border:1px solid #e4e4e4;background:#fafafa;font-size:9px;color:#bbb;padding:5px 9px}
.search svg{position:absolute;right:7px;top:4px}

/* sidebar column */
.sidebar{left:548px;top:121px;width:239px;height:946px;background:var(--side);border-left:1px solid #e0e0e0;border-right:1px solid #e0e0e0}

/* cards */
.card{background:var(--white);box-shadow:0 1px 3px rgba(0,0,0,.18);left:55px;width:470px}
.tab{left:20px;width:42px;background:var(--rose);color:var(--white);text-align:center}
.tab .day{font-size:21px;line-height:1;margin-top:6px;display:block}
.tab .month{font-size:12px;display:block;line-height:1.2}
.tab .year{font-size:11px;font-weight:700;display:block;line-height:1.2}

.quote-text{left:55px;width:470px;top:164px;text-align:center;font-size:18.5px;font-weight:700;color:var(--ink)}
.quote-source{left:55px;width:427px;top:198px;text-align:right;font-size:9px;color:var(--red);font-weight:700;text-transform:uppercase}

.post-title{left:80px;font-size:22px;color:var(--muted);line-height:27px;width:360px}
.share{display:flex;gap:5px}
.share i{display:block;width:20px;height:20px;background:#4a6aa5;border-radius:2px}
.share i+i{background:#5cb5e0}
.post-body{left:80px;width:420px;font-size:13.5px;line-height:19.6px;text-align:justify;color:var(--text)}
.post-body p+p{margin-top:19.6px}
.photo{left:80px;width:420px;height:224px;background:#d6d6d6;padding:5px}
.photo div{width:100%;height:100%;background:linear-gradient(180deg,#4d5a8c 0%,#6a6b55 45%,#9b4a34 62%,#2c2a1e 100%)}
.post-meta{left:73px;width:427px;height:18px;background:#ededed;font-family:"Crimson Text",Georgia,serif;font-style:italic;font-size:12px;line-height:18px;color:#777;padding:0 10px 0 26px}
.post-meta .bubble{position:absolute;left:8px;top:5px}
.post-meta .more{position:absolute;right:12px;top:0;color:var(--red)}
.post-meta .more.plain{color:#555}

.pager{left:148px;top:978px;display:flex;gap:8px}
.pager a{display:block;height:22px;min-width:27px;background:var(--white);border:1px solid #e2e2e2;font-size:10px;color:#aaa;text-align:center;line-height:20px;text-decoration:none;padding:0 8px}
.pager a.current{background:var(--red);color:var(--white);border-color:var(--red);font-weight:700}
.pager a.wide{min-width:54px}

/* sidebar content */
.follow{left:578px;top:137px;width:182px;height:28px;background:var(--white);border:1px solid #ddd;box-shadow:0 1px 2px rgba(0,0,0,.1);font-size:13.5px;color:#777;line-height:26px;padding-left:44px}
.follow svg{position:absolute;left:12px;top:5px}
.rule{left:549px;width:237px;height:1px;background:var(--line)}
.side-head{left:563px;font-size:13.5px;color:#8a8a8a}
.side-text{left:563px;width:210px;font-size:9px;line-height:13.3px;color:#555;text-align:justify}
.side-link{left:563px;font-size:9px;color:var(--faint);text-decoration:underline}
.side-link.hot{color:var(--red)}
.avatar{left:566px;top:212px;width:91px;height:71px;background:#555;border:4px solid #d9d9d9}
.map{left:572px;top:490px;width:190px;height:90px;background:linear-gradient(135deg,#e6e1d6,#d4cfc2);border:4px solid #d4d4d4}
.side-list li{font-size:9px;line-height:13.3px;color:#555}
.side-list.bullets li::before{content:"• ";color:#888}

/* footer */
.footer{left:0;top:1067px;width:825px;height:133px;background:var(--foot)}
.foot-col{top:1081px}
.foot-col h4{font-size:9.5px;font-weight:700;color:var(--white);margin-bottom:9px}
.foot-col li{font-size:9px;color:#d8d8d8;line-height:13.5px;padding-left:11px;position:relative}
.foot-col li::before{content:"";position:absolute;left:2px;top:6px;width:3px;height:3px;background:#d8d8d8;border-radius:50%}
.foot-brand{left:570px;top:1112px;display:flex;align-items:center;gap:8px;font-size:22px;color:#e8e8e8}
.foot-brand i{display:block;width:20px;height:20px;border-radius:50%;background:#e8e8e8}
</style>
</head>
<body>

<header>
  <nav class="topbar abs">
    <svg class="mark abs" width="16" height="15" viewBox="0 0 16 15"><circle cx="8" cy="7.5" r="5" fill="#fff"/></svg>
    <div class="menu abs">
      <a class="active" href="#">Mission Blogs</a>
      <a href="#">Opportunities</a>
      <a href="#">Option3</a>
      <a href="#">Option4</a>
    </div>
    <div class="account abs">SIGN IN<span>|</span>REGISTER</div>
  </nav>

  <div class="masthead abs">
    <h1 class="owner-name abs" style="font-weight:400">Hannah Brooks</h1>
    <div class="owner-org abs">Kairo Australia</div>
    <div class="search abs">Search
      <svg width="12" height="12" viewBox="0 0 12 12"><circle cx="5" cy="5" r="3.6" fill="none" stroke="#888" stroke-width="1.6"/><line x1="7.6" y1="7.6" x2="11" y2="11" stroke="#888" stroke-width="1.8"/></svg>
    </div>
  </div>
</header>

<aside class="sidebar abs"></aside>

<main>
  <!-- quote -->
  <div class="card abs" style="top:137px;height:91px"></div>
  <div class="tab abs" style="top:152px;height:61px">
    <svg width="42" height="61" viewBox="0 0 42 61"><ellipse cx="21" cy="29" rx="10" ry="7" fill="#fff"/><path d="M15 33 L13 40 L20 35 Z" fill="#fff"/></svg>
  </div>
  <blockquote class="quote-text abs">"Sympathy is no substitute for action."</blockquote>
  <div class="quote-source abs">— Elias Harrow</div>

  <!-- post one -->
  <article>
    <div class="card abs" style="top:243px;height:499px"></div>
    <div class="tab abs" style="top:260px;height:60px"><span class="day">01</span><span class="month">July</span><span class="year">2011</span></div>
    <h2 class="post-title abs" style="top:253px;font-weight:400">Just Arrived</h2>
    <div class="share abs" style="left:455px;top:255px"><i></i><i></i></div>
    <div class="post-body abs" style="top:287px">
      <p>Lorem ipsum dolor sit amet, consectetuer adipiscing elit. Aenean commodo ligula eget dolor. Aenean massa. Cum sociis natoque penatibus et magnis dis parturient montes, nascetur ridiculus mu. Donec quam felis, ultricies nec, pellentesque eu, pretium quis, sem. Nulla consequat massa quisburitjusto. Nullam dictum felis eu pede mollis pretium. Integer tincidunt. Cras dapibus.</p>
      <p>Enim. Aliquam lorem ante, dapibus in, viverra quis, feugiat a, tellus. Phasellus viverra nulla ut metus varius laoreet.</p>
    </div>
    <div class="photo abs" style="top:470px" role="img" aria-label="Photo of a red brick mission house among trees under a blue sky"><div></div></div>
    <div class="post-meta abs" style="top:710px">
      <svg class="bubble" width="11" height="9" viewBox="0 0 11 9"><ellipse cx="5.5" cy="3.5" rx="5" ry="3.3" fill="var(--red)"/><path d="M3 6 L2 9 L6 6.5Z" fill="var(--red)"/></svg>
      4 comments<span class="more">Read more</span>
    </div>
  </article>

  <!-- post two -->
  <article>
    <div class="card abs" style="top:757px;height:201px"></div>
    <div class="tab abs" style="top:774px;height:60px"><span class="day">01</span><span class="month">July</span><span class="year">2011</span></div>
    <h2 class="post-title abs" style="top:766px;font-weight:400">Only 14 days to go before I fly for Malawi</h2>
    <div class="share abs" style="left:455px;top:768px"><i></i><i></i></div>
    <div class="post-body abs" style="top:830px">
      <p>Lorem ipsum dolor sit amet, consectetuer adipiscing elit. Aenean commodo ligula eget dolor. Aenean massa. Cum sociis natoque penatibus et magnis dis parturient montes, nascetur ridiculus mus. Donec quum dolor sit amet, consectetuer</p>
    </div>
    <div class="post-meta abs" style="top:928px">
      <svg class="bubble" width="11" height="9" viewBox="0 0 11 9"><ellipse cx="5.5" cy="3.5" rx="5" ry="3.3" fill="var(--red)"/><path d="M3 6 L2 9 L6 6.5Z" fill="var(--red)"/></svg>
      4 comments<span class="more plain">Read more</span>
    </div>
  </article>

  <nav class="pager abs">
    <a class="wide" href="#">Previous</a>
    <a class="current" href="#">1</a>
    <a href="#">2</a><a href="#">3</a><a href="#">4</a><a href="#">5</a>
    <a class="wide" href="#">Next</a>
  </nav>
</main>

<!-- sidebar widgets -->
<div class="follow abs">
  <svg width="17" height="17" viewBox="0 0 17 17"><circle cx="8.5" cy="8.5" r="8" fill="#e4e4e4" stroke="#ccc"/><path d="M8.5 4.5v8M4.5 8.5h8" stroke="#777" stroke-width="1.6"/></svg>
  Follow Hannah Brooks
</div>
<div class="rule abs" style="top:183px"></div>

<h3 class="side-head abs" style="top:190px;font-weight:400">About Hannah</h3>
<div class="avatar abs"></div>
<p class="side-text abs" style="left:667px;width:106px;top:213px">Lorem ipsum dolor sit amet, consectetuer adipiscing elit. Aenean commodo ligula eget dolor. Aenean</p>
<a class="side-link abs" style="top:298px" href="#">View my complete profile</a>
<div class="rule abs" style="top:322px"></div>

<h3 class="side-head abs" style="top:328px;font-weight:400">About Hannah's Ministry</h3>
<p class="side-text abs" style="top:351px">Lorem ipsum dolor sit amet, consectetuer adipiscing elit. Aenean commodo ligula eget dolor. Aenean Lorem ipsum dolor sit amet, consectetuer adipiscing elit. Aenean commodo ligula eget dolor. Aenea Lorem ipsum</p>
<a class="side-link hot abs" style="top:436px" href="#">Read more</a>
<div class="rule abs" style="top:458px"></div>

<h3 class="side-head abs" style="top:466px;font-weight:400">About Malawi</h3>
<div class="map abs" role="img" aria-label="Street map of the area around the mission base in Malawi"></div>
<p class="side-text abs" style="top:589px">Lorem ipsum dolor sit amet, consectetuer adipiscing elit. Aenean commodo ligula eget dolor. Aenean Lorem</p>
<a class="side-link abs" style="top:641px" href="#">Read more</a>
<div class="rule abs" style="top:662px"></div>

<h3 class="side-head abs" style="top:670px;font-weight:400">Kairo Events</h3>
<ul class="side-list abs" style="left:563px;top:692px">
  <li>Kairo Prayer Event - May 15th</li>
  <li>Kairo Conference - June 30th</li>
</ul>
<a class="side-link abs" style="top:728px" href="#">Read more</a>
<div class="rule abs" style="top:747px"></div>

<h3 class="side-head abs" style="top:755px;font-weight:400">Kairo Events</h3>
<ul class="side-list bullets abs" style="left:566px;top:777px">
  <li>Teacher in Blanta (2yrs)</li>
  <li>Financial Controller (long term)</li>
  <li>Project Manager (6months+)</li>
  <li>Bible College Lecturer (long term)</li>
</ul>
<a class="side-link abs" style="top:835px" href="#">Read more</a>

<footer class="footer abs"></footer>
<div class="foot-col abs" style="left:52px">
  <h4>About Us</h4>
  <ul><li>About FaithPostly</li><li>Missionaries</li><li>Mission Agencies</li><li>Churches</li><li>Mission Supporters</li><li>Privacy</li></ul>
</div>
<div class="foot-col abs" style="left:183px">
  <h4>Regions Mission</h4>
  <ul><li>Africa</li><li>Asia</li><li>North America</li><li>Latin America</li><li>Aust/Pacific</li></ul>
</div>
<div class="foot-col abs" style="left:335px">
  <h4>Agencies</h4>
  <ul><li>Corvane</li><li>Tidewell Global</li><li>Kairo Australia</li><li>Westel</li></ul>
</div>
<div class="foot-brand abs"><i></i>faithpostly.org</div>

</body>
</html>
```